Need Business Card ASAP

We need a business card design for a meeting coming up in a few days. The company name is Harwick Development and Construction and the logo is attached. Something clean, cool, and contemporary that we can get to a printer right away. Attached is the business card for Molvar Energy, an affiliated company, which we like. Instead of the hawk on the back, you could use the attached "D". We'll also be needing matching letterhead in the near future, so ideas for that are welcome.

```html
<!DOCTYPE html>
<html lang="en">
<head>
<meta charset="utf-8">
<title>Harwick Development and Construction – Business Card</title>
<link rel="stylesheet" href="https://fonts.googleapis.com/css2?family=Exo+2:wght@400;500;600&display=swap">
<style>
  :root {
    --bg: #ece8e1;
    --card: #ffffff;
    --gold-light: #e9e3c6;
    --gold: #c9bd8e;
    --gold-deep: #b2a574;
    --ink: #231f20;
    --paper-text: #f4f1e6;
  }
  * { box-sizing: border-box; margin: 0; padding: 0; }
  html, body { width: 1200px; height: 672px; overflow: hidden; }
  body {
    background: var(--bg);
    font-family: "Exo 2", sans-serif;
    color: var(--ink);
    position: relative;
  }
  .card {
    position: absolute;
    top: 66px;
    width: 310px;
    height: 540px;
    background: var(--card);
    box-shadow: 0 6px 24px rgba(0,0,0,.18);
    overflow: hidden;
  }
  .card--front { left: 255px; }
  .card--back  { left: 635px; }

  /* front */
  .front-panel {
    position: absolute;
    left: 14px; right: 14px; top: 18px;
    height: 400px;
    border-radius: 22px 22px 0 0;
    background: radial-gradient(ellipse at 55% 55%, var(--gold-light) 0%, var(--gold) 55%, var(--gold-deep) 100%);
  }
  .identity {
    position: absolute;
    top: 26px; left: 0; right: 0;
    text-align: center;
  }
  .identity__name {
    font-size: 22px;
    font-weight: 500;
    letter-spacing: 1px;
    padding-bottom: 6px;
    border-bottom: 2px solid var(--ink);
  }
  .identity__role {
    font-size: 14px;
    font-weight: 500;
    letter-spacing: 2px;
    padding-top: 6px;
  }
  .contact-list {
    list-style: none;
    position: absolute;
    top: 118px; left: 34px; right: 16px;
  }
  .contact-list li {
    display: flex;
    align-items: center;
    gap: 12px;
    height: 40px;
    font-size: 16px;
    letter-spacing: 1px;
    white-space: nowrap;
  }
  .contact-list li.small { font-size: 14px; letter-spacing: .4px; }
  .contact-icon { width: 22px; height: 22px; flex: none; }
  .front-band {
    position: absolute;
    left: 14px; right: 14px; bottom: 18px;
    height: 128px;
    background: var(--ink);
    border-radius: 0 26px 0 0;
    color: var(--paper-text);
    display: flex;
    align-items: center;
    gap: 16px;
    padding: 0 26px;
  }
  .front-band address {
    font-style: normal;
    font-size: 15px;
    line-height: 1.45;
    letter-spacing: .5px;
    white-space: nowrap;
  }
  .front-band .contact-icon { width: 28px; height: 28px; }

  /* back */
  .back-bar {
    position: absolute;
    left: 40px; right: 40px; top: 22px;
    height: 16px;
    border-radius: 8px;
    background: var(--ink);
  }
  .brand {
    position: absolute;
    top: 150px; left: 0; right: 0;
    display: flex;
    flex-direction: column;
    align-items: center;
    gap: 18px;
  }
  .brand__square {
    width: 64px; height: 64px;
    background: var(--gold);
  }
  .brand__name {
    color: var(--ink);
    font-weight: 500;
    text-align: center;
    line-height: 1.25;
  }
  .brand__name .main { display: block; font-size: 30px; letter-spacing: 1px; }
  .brand__name .sub  { display: block; font-size: 11px; letter-spacing: 2.5px; text-transform: uppercase; }
</style>
</head>
<body>

<section class="card card--front" aria-label="Business card front">
  <div class="front-panel">
    <div class="identity">
      <h1 class="identity__name">ELENA MARSH</h1>
      <p class="identity__role">GENERAL MANAGER</p>
    </div>
    <ul class="contact-list">
      <li>
        <svg class="contact-icon" viewBox="0 0 24 24" aria-hidden="true"><circle cx="12" cy="12" r="11" fill="none" stroke="#231f20" stroke-width="1.6"/><path d="M8.5 6.5c-1 1-1.2 2.8.3 5.3s3.4 4.2 5.5 4.7c1.2.3 2-.3 2.5-1l-2-1.8-1.3.9c-1-.5-2.4-1.9-2.9-2.9l.9-1.3-1.8-2z" fill="#231f20"/></svg>
        <span>012 555 0147</span>
      </li>
      <li>
        <svg class="contact-icon" viewBox="0 0 24 24" aria-hidden="true"><circle cx="12" cy="12" r="11" fill="none" stroke="#231f20" stroke-width="1.6"/><rect x="8.5" y="5.5" width="7" height="13" rx="1.2" fill="#231f20"/><rect x="9.7" y="7" width="4.6" height="8.5" fill="#d8cfa8"/></svg>
        <span>012 555 0148</span>
      </li>
      <li>
        <svg class="contact-icon" viewBox="0 0 24 24" aria-hidden="true"><circle cx="12" cy="12" r="11" fill="none" stroke="#231f20" stroke-width="1.6"/><rect x="6.5" y="10" width="11" height="7" rx="1" fill="#231f20"/><rect x="8.5" y="6.5" width="7" height="4" fill="none" stroke="#231f20" stroke-width="1.3"/></svg>
        <span>012 555 0149</span>
      </li>
      <li class="small">
        <svg class="contact-icon" viewBox="0 0 24 24" aria-hidden="true"><circle cx="12" cy="12" r="11" fill="none" stroke="#231f20" stroke-width="1.6"/><rect x="6.5" y="8" width="11" height="8" rx="1" fill="#231f20"/><path d="M6.8 8.4 12 12.4l5.2-4" fill="none" stroke="#d8cfa8" stroke-width="1.2"/></svg>
        <span>elena@harwickdc.com</span>
      </li>
      <li class="small">
        <svg class="contact-icon" viewBox="0 0 24 24" aria-hidden="true"><circle cx="12" cy="12" r="11" fill="none" stroke="#231f20" stroke-width="1.6"/><circle cx="12" cy="12" r="6" fill="none" stroke="#231f20" stroke-width="1.3"/><ellipse cx="12" cy="12" rx="2.6" ry="6" fill="none" stroke="#231f20" stroke-width="1.1"/><path d="M6 12h12" stroke="#231f20" stroke-width="1.1"/></svg>
        <span>www.harwickdc.com</span>
      </li>
    </ul>
  </div>
  <div class="front-band">
    <svg class="contact-icon" viewBox="0 0 24 24" aria-hidden="true"><circle cx="12" cy="12" r="11" fill="none" stroke="#f4f1e6" stroke-width="1.6"/><path d="M12 5.5a4.3 4.3 0 0 0-4.3 4.3c0 3.2 4.3 8.2 4.3 8.2s4.3-5 4.3-8.2A4.3 4.3 0 0 0 12 5.5z" fill="#f4f1e6"/><circle cx="12" cy="9.8" r="1.6" fill="#231f20"/></svg>
    <address>27 Calder Road<br>4th building North Str.</address>
  </div>
</section>

<section class="card card--back" aria-label="Business card back">
  <div class="back-bar"></div>
  <div class="brand">
    <div class="brand__square"></div>
    <p class="brand__name">
      <span class="main">Harwick</span>
      <span class="sub">Development and Construction</span>
    </p>
  </div>
</section>

</body>
</html>
```